Harbor Crest Renewal Business Cards

We need a sleek and sexy business card design

Contact Information for Business Card

Name, address, phone number, email. Vincent Morrasco 482 Pellham Street Suite 200C Marrow Glen NY 11958 (631)555-0174 Also a second version with the name Derek Halvorn

```html
<!DOCTYPE html>
<html lang="en">
<head>
<meta charset="utf-8">
<title>Harbor Crest Renewal — Business Card Proof</title>
<link rel="stylesheet" href="https://fonts.googleapis.com/css2?family=Hind:wght@400;500&family=Montserrat:wght@600;700&display=swap">
<style>
  :root{
    --paper:#ffffff;
    --ink:#231f20;
    --brand-orange:#cf3d06;
    --brand-blue:#00448a;
    --contact-yellow:#e6e81e;
    --safe-line:#e2e2e2;
    --mark:#231f20;
  }
  html,body{margin:0;padding:0;overflow:hidden;background:var(--paper);}
  .sheet{position:relative;width:1200px;height:1200px;overflow:hidden;background:var(--paper);font-family:"Hind",Arial,sans-serif;}
  .crop-marks{position:absolute;inset:0;}
  .side-label{position:absolute;left:0;width:1264px;text-align:center;font-family:Arial,Helvetica,sans-serif;font-size:33px;color:var(--ink);}
  .side-label--front{top:27px;}
  .side-label--back{top:597px;}
  .trim{position:absolute;left:193px;width:815px;height:489px;border:2px solid var(--mark);box-sizing:border-box;}
  .trim--front{top:82px;}
  .trim--back{top:650px;}
  .card-front{position:absolute;left:220px;top:105px;width:760px;height:435px;border:2px solid var(--safe-line);box-sizing:border-box;background:var(--paper);}
  .brand-lockup{position:absolute;left:0;right:0;top:238px;display:flex;align-items:center;justify-content:center;gap:16px;}
  .brand-square{width:34px;height:34px;background:var(--brand-blue);}
  .brand-name{font-family:"Montserrat",Arial,sans-serif;font-weight:700;font-size:44px;color:var(--brand-blue);letter-spacing:.5px;}
  .card-back{position:absolute;left:220px;top:674px;width:760px;height:434px;overflow:hidden;background:var(--brand-orange);}
  .card-back__wave{position:absolute;inset:0;}
  .holder-name{position:absolute;left:0;width:760px;top:182px;margin:0;text-align:center;font-size:46px;line-height:60px;color:var(--ink);font-weight:400;}
  .contact{position:absolute;margin:0;color:var(--contact-yellow);font-size:17px;line-height:20px;}
  .contact--address{left:30px;top:358px;}
  .contact--address .indent{padding-left:69px;display:block;}
  .contact--reach{left:437px;top:381px;}
</style>
</head>
<body>
<main class="sheet">
  <svg class="crop-marks" width="1200" height="1200" viewBox="0 0 1200 1200" aria-hidden="true">
    <g stroke="#231f20" stroke-width="1" fill="none">
      <line x1="220" y1="47" x2="220" y2="80"/><line x1="987" y1="47" x2="987" y2="80"/>
      <line x1="165" y1="110" x2="193" y2="110"/><line x1="1007" y1="110" x2="1035" y2="110"/>
      <line x1="165" y1="538" x2="193" y2="538"/><line x1="1007" y1="545" x2="1035" y2="545"/>
      <line x1="220" y1="573" x2="220" y2="598"/><line x1="987" y1="573" x2="987" y2="598"/>
      <line x1="220" y1="616" x2="220" y2="648"/><line x1="987" y1="616" x2="987" y2="648"/>
      <line x1="165" y1="678" x2="193" y2="678"/><line x1="1007" y1="678" x2="1035" y2="678"/>
      <line x1="165" y1="1106" x2="193" y2="1106"/><line x1="1007" y1="1112" x2="1035" y2="1112"/>
      <line x1="220" y1="1141" x2="220" y2="1166"/><line x1="987" y1="1141" x2="987" y2="1166"/>
    </g>
  </svg>

  <div class="side-label side-label--front">Front</div>
  <div class="trim trim--front"></div>
  <section class="card-front">
    <div class="brand-lockup">
      <span class="brand-square"></span>
      <span class="brand-name">Harbor Crest Renewal</span>
    </div>
  </section>

  <div class="side-label side-label--back">Back</div>
  <div class="trim trim--back"></div>
  <section class="card-back">
    <svg class="card-back__wave" width="760" height="434" viewBox="0 0 760 434" aria-hidden="true">
      <path d="M0,171 C150,262 320,322 480,324 C630,324 700,296 760,384 L760,434 L0,434 Z" fill="var(--brand-blue)"/>
    </svg>
    <h1 class="holder-name">Vincent Morrasco</h1>
    <p class="contact contact--address">Address: 482 Pellham Street<span class="indent">Suite 200C Marrow Glen</span><span class="indent">NY 11958</span></p>
    <p class="contact contact--reach">phone number: (631)555-0174<br>email: www.Harbor Crest Renewal.com</p>
  </section>
</main>
</body>
</html>
```